Header and footer for report

We would like a header and footer for our building management reports that incorporate a modern city skyline and our logo.

As well as update our other stationery.

```html
<!DOCTYPE html>
<html lang="en">
<head>
<meta charset="utf-8">
<title>Norvale Group Stationery</title>
<link rel="stylesheet" href="https://fonts.googleapis.com/css2?family=Didact+Gothic&family=Quicksand:wght@700&display=swap">
<style>
  :root {
    --blue: #1b63ad;
    --blue-bright: #2a7fd4;
    --sky-pale: #dbe6f1;
    --sky-faint: #eef3f9;
    --ink: #111111;
    --text: #333333;
    --paper: #ffffff;
    --bg: #ffffff;
    --shadow: rgba(60, 110, 170, 0.18);
  }
  * { box-sizing: border-box; margin: 0; padding: 0; }
  html, body { width: 1050px; height: 1200px; overflow: hidden; background: var(--bg); }
  body { position: relative; font-family: "Didact Gothic", sans-serif; color: var(--text); }

  .sheet { position: absolute; background: var(--paper); box-shadow: 0 0 14px var(--shadow); overflow: hidden; }
  .wordmark { font-family: "Quicksand", sans-serif; font-weight: 700; color: var(--blue); white-space: nowrap; letter-spacing: 0.5px; }

  /* Letterhead */
  .letterhead { left: 25px; top: 256px; width: 408px; height: 527px; }
  .letterhead .wordmark { position: absolute; left: 19px; top: 66px; font-size: 15px; }
  .letterhead .contact { position: absolute; right: 40px; top: 19px; text-align: right; font-size: 9.5px; line-height: 11.5px; color: var(--text); }
  .letterhead .contact p { margin-bottom: 4px; }
  .letterhead .icon-strip { position: absolute; right: 19px; top: 19px; width: 15px; height: 56px; background: var(--blue); border-radius: 2px; display: flex; flex-direction: column; justify-content: space-around; align-items: center; }
  .letterhead .skyline { position: absolute; left: 0; right: 0; top: 387px; height: 105px; background: linear-gradient(to top, #c9daec, var(--sky-faint)); }
  .letterhead .footer-band { position: absolute; left: 0; right: 0; top: 492px; height: 29px; background: var(--ink); color: #fff; font-size: 10px; display: flex; justify-content: space-between; align-items: center; padding: 0 19px; }
  .letterhead .footer-band span { display: flex; align-items: center; gap: 4px; }
  .letterhead .footer-rule { position: absolute; left: 0; right: 0; top: 521px; height: 6px; background: var(--blue); }

  /* Business card front */
  .card-front { left: 473px; top: 256px; width: 553px; height: 316px; }
  .card-front .wordmark { position: absolute; left: 0; right: 0; top: 118px; text-align: center; font-size: 36px; }
  .skyline-band { position: absolute; left: 0; right: 0; bottom: 0; background: linear-gradient(to bottom, var(--sky-pale) 0%, var(--sky-pale) 35%, var(--blue) 70%, var(--blue) 100%); }
  .card-front .skyline-band { height: 158px; }

  /* Business card back */
  .card-back { left: 473px; top: 626px; width: 553px; height: 317px; }
  .card-back .person { position: absolute; left: 20px; top: 16px; }
  .card-back .person-name { font-family: "Quicksand", sans-serif; font-weight: 700; color: var(--blue-bright); font-size: 22px; line-height: 26px; }
  .card-back .person-role { font-size: 17px; line-height: 22px; color: var(--text); }
  .card-back .wordmark { position: absolute; right: 24px; top: 58px; font-size: 11px; }
  .card-back .divider { position: absolute; left: 20px; right: 22px; top: 83px; border-top: 2px dotted #555; }
  .card-back .details { position: absolute; top: 100px; font-size: 13px; line-height: 16px; color: var(--text); }
  .card-back .details li { list-style: none; display: flex; gap: 6px; margin-bottom: 9px; }
  .card-back .details.left { left: 20px; }
  .card-back .details.right { left: 333px; }
  .card-back .skyline-band { height: 140px; }

  .ico { width: 14px; height: 14px; flex: none; }
  .icon-strip .ico { width: 10px; height: 10px; }
</style>
</head>
<body>

<svg width="0" height="0" style="position:absolute">
  <defs>
    <symbol id="i-pin" viewBox="0 0 16 16"><path d="M8 1a5 5 0 0 0-5 5c0 3.5 5 9 5 9s5-5.5 5-9a5 5 0 0 0-5-5zm0 7a2 2 0 1 1 0-4 2 2 0 0 1 0 4z" fill="currentColor"/></symbol>
    <symbol id="i-phone" viewBox="0 0 16 16"><path d="M4 1.5l2.2 3-1.3 1.6c.8 1.8 2.2 3.2 4 4l1.6-1.3 3 2.2-1.3 2.4C7.6 13.3 2.7 8.4 1.6 3.8z" fill="currentColor"/></symbol>
    <symbol id="i-fax" viewBox="0 0 16 16"><path d="M4 1h8v4H4zM2 6h12v6h-2v3H4v-3H2zm3 4v4h6v-4z" fill="currentColor"/></symbol>
    <symbol id="i-mail" viewBox="0 0 16 16"><path d="M1 4h14v9H1zm1 1l6 4.5L14 5z" fill="currentColor"/></symbol>
    <symbol id="i-globe" viewBox="0 0 16 16"><circle cx="8" cy="8" r="6.5" fill="none" stroke="currentColor" stroke-width="1.3"/><path d="M1.5 8h13M8 1.5c-3 3.5-3 9.5 0 13M8 1.5c3 3.5 3 9.5 0 13" fill="none" stroke="currentColor" stroke-width="1.1"/></symbol>
  </defs>
</svg>

<section class="sheet letterhead">
  <div class="wordmark">NORVALE GROUP</div>
  <div class="contact">
    <p>Unit 7 / 18 Harbourview Road<br>Elmsford, NSW 2140</p>
    <p>1300 00NORV (6678)</p>
    <p>Fax: 8021 3390</p>
  </div>
  <div class="icon-strip" style="color:#fff">
    <svg class="ico"><use href="#i-pin"/></svg>
    <svg class="ico"><use href="#i-phone"/></svg>
    <svg class="ico"><use href="#i-fax"/></svg>
  </div>
  <div class="skyline" role="img" aria-label="Faint pale blue city skyline silhouette"></div>
  <div class="footer-band">
    <span><svg class="ico" style="color:var(--blue-bright);width:10px;height:10px"><use href="#i-globe"/></svg>www.norvalegroup.com.au</span>
    <span><svg class="ico" style="color:var(--blue-bright);width:11px;height:11px"><use href="#i-mail"/></svg>admin@norvalegroup.com.au</span>
  </div>
  <div class="footer-rule"></div>
</section>

<section class="sheet card-front">
  <div class="wordmark">NORVALE GROUP</div>
  <div class="skyline-band" role="img" aria-label="Blue and pale blue city skyline silhouette"></div>
</section>

<section class="sheet card-back">
  <div class="person">
    <div class="person-name">Name Surname</div>
    <div class="person-role">CEO, Norvale Group</div>
  </div>
  <div class="wordmark">NORVALE GROUP</div>
  <div class="divider"></div>
  <ul class="details left">
    <li><svg class="ico" style="color:var(--blue)"><use href="#i-phone"/></svg>1300 00NORV (6678)</li>
    <li><svg class="ico" style="color:var(--blue)"><use href="#i-pin"/></svg>Unit 7 / 18 Harbourview Road,<br>Elmsford, NSW 2140</li>
  </ul>
  <ul class="details right">
    <li><svg class="ico" style="color:var(--blue)"><use href="#i-mail"/></svg>admin@norvalegroup.com.au</li>
    <li><svg class="ico" style="color:var(--blue)"><use href="#i-globe"/></svg>www.norvalegroup.com.au</li>
  </ul>
  <div class="skyline-band" role="img" aria-label="Blue and pale blue city skyline silhouette"></div>
</section>

</body>
</html>
```